Children's Party Business needs a Business Card design!

We need a double sided, colour business card design.
The company name is "Maplewood Kids' Celebrations". We want one side to feature this logo.
We want the second side to feature the two branches "The Caped Crusade Adventure" and "The Fairytale Gala Adventure". I have attached logos for each of these below. When using these, I suggest removing the tagline & image from the logos, as those elements are already featured in the "Maplewood Kids' Celebration" logo.
To be included:
www.maplewoodkidscelebrations.com.au
1300 471 608
Optional text- "Making Dreams a Reality"
Optional photos- I've attached a bunch of our Character photos, which can be used if you please!
To give you an idea of the business, see The Caped Crusade Adventure website (under development):
http://qorvint.com/demo/capedcrusadeadventure/
Target Market(s)
Parents
Industry/Entity Type
Business
Contact Information for Business Card
To be included:
1300 471 608
Colors
Designer to choose colors to be used in the design.
Look and feel

```html
<!DOCTYPE html>
<html lang="en">
<head>
<meta charset="utf-8">
<title>Maplewood Kids' Celebrations – Business Card</title>
<link rel="stylesheet" href="https://fonts.googleapis.com/css2?family=Fredoka:wght@500;600&family=Short+Stack&display=swap">
<style>
  :root {
    --bg: #e9e9e9;
    --card: #f7f7f7;
    --navy: #1f2a63;
    --orange: #f0892a;
    --green: #86be3a;
    --sky: #6fb6e2;
    --violet: #7b5cb8;
    --red: #e0455a;
    --magenta: #c9268f;
    --teal: #4bb8c0;
    --ink: #1f2545;
  }
  * { box-sizing: border-box; margin: 0; padding: 0; }
  html, body { width: 1200px; height: 576px; overflow: hidden; }
  body { background: var(--bg); position: relative; font-family: "Short Stack", "Comic Sans MS", cursive; }

  .card {
    position: absolute; top: 138px; width: 480px; height: 294px;
    background: var(--card); border-radius: 11px; overflow: hidden;
    box-shadow: 0 3px 6px rgba(0,0,0,.18);
  }
  .card--front { left: 84px; }
  .card--back { left: 602px; }

  /* front */
  .pastel-strip { position: absolute; top: 0; left: 0; right: 0; height: 42px; display: flex; }
  .pastel-strip span { flex: 1; }
  .pastel-strip span:nth-child(1) { background: linear-gradient(#f9dcc0, rgba(247,247,247,0)); }
  .pastel-strip span:nth-child(2) { background: linear-gradient(#d9ecc6, rgba(247,247,247,0)); }
  .pastel-strip span:nth-child(3) { background: linear-gradient(#d3e8f5, rgba(247,247,247,0)); }
  .pastel-strip span:nth-child(4) { background: linear-gradient(#dcd5ec, rgba(247,247,247,0)); }
  .pastel-strip span:nth-child(5) { background: linear-gradient(#f5d2d6, rgba(247,247,247,0)); }
  .pastel-strip span:nth-child(6) { background: linear-gradient(#d3d6e0, rgba(247,247,247,0)); }
  .pastel-strip span:nth-child(7) { background: linear-gradient(#f3d0e6, rgba(247,247,247,0)); }

  .colour-band { position: absolute; bottom: 0; left: 0; right: 0; height: 6px; display: flex; }
  .colour-band span { flex: 1; }
  .colour-band span:nth-child(1) { background: var(--orange); }
  .colour-band span:nth-child(2) { background: var(--green); }
  .colour-band span:nth-child(3) { background: var(--sky); }
  .colour-band span:nth-child(4) { background: var(--violet); }
  .colour-band span:nth-child(5) { background: var(--red); }
  .colour-band span:nth-child(6) { background: var(--navy); }
  .colour-band span:nth-child(7) { background: var(--magenta); }

  .brand { position: absolute; left: 98px; top: 58px; width: 296px; height: 140px; }
  .brand__hero {
    position: absolute; left: 0; top: 0; width: 66px; height: 140px; border-radius: 8px;
    background: linear-gradient(180deg, #f2a0c4 0%, #7fc7d9 22%, #2a3a7a 40%, #1f2a63 100%);
  }
  .brand__fairy {
    position: absolute; right: 0; top: 36px; width: 84px; height: 92px; border-radius: 8px;
    background: linear-gradient(160deg, #a9d6f2 0%, #6fb6e2 35%, #1f2a63 100%);
  }
  .brand__name {
    position: absolute; left: 68px; top: 38px; width: 146px;
    font-family: "Fredoka", sans-serif; font-weight: 600; font-size: 21px; line-height: 1.05;
    color: var(--navy); text-align: center;
  }

  /* back */
  .swoosh { position: absolute; inset: 0; }
  .tagline {
    position: absolute; right: 28px; top: 24px; color: #fff; text-align: right;
    font-size: 13px; line-height: 1.35;
  }
  .phone {
    position: absolute; left: 30px; top: 88px;
    font-family: "Fredoka", sans-serif; font-weight: 600; font-size: 31px; letter-spacing: 1px;
  }
  .phone .d1 { color: var(--violet); } .phone .d2 { color: var(--teal); }
  .phone .d3 { color: var(--orange); } .phone .d4 { color: var(--red); }
  .phone .d5 { color: var(--green); } .phone .d6 { color: var(--magenta); }
  .phone .gap { display: inline-block; width: 16px; }
  .contact { position: absolute; left: 29px; top: 130px; font-size: 13.5px; line-height: 20px; color: var(--ink); }

  .branches { position: absolute; left: 28px; top: 190px; right: 28px; display: flex; justify-content: space-between; }
  .branch {
    font-family: "Fredoka", sans-serif; font-weight: 600; font-size: 20px; line-height: 1.08;
    color: var(--navy); text-align: center;
  }
  .branch--fairytale { width: 220px; }
  .branch--caped { width: 190px; }
</style>
</head>
<body>

<section class="card card--front" aria-label="Card front">
  <div class="pastel-strip"><span></span><span></span><span></span><span></span><span></span><span></span><span></span></div>
  <div class="brand">
    <div class="brand__hero" role="img" aria-label="Illustration of a caped superhero silhouette holding party balloons"></div>
    <p class="brand__name">Maplewood Kids' Celebrations</p>
    <div class="brand__fairy" role="img" aria-label="Illustration of a dancing fairy silhouette with blue wings"></div>
  </div>
  <div class="colour-band"><span></span><span></span><span></span><span></span><span></span><span></span><span></span></div>
</section>

<section class="card card--back" aria-label="Card back">
  <svg class="swoosh" width="480" height="294" viewBox="0 0 480 294" aria-hidden="true">
    <defs>
      <linearGradient id="swooshFill" x1="0" y1="0" x2="1" y2="0">
        <stop offset="0" stop-color="#c9268f"/>
        <stop offset="0.5" stop-color="#6b2a8a"/>
        <stop offset="1" stop-color="#1f2a63"/>
      </linearGradient>
    </defs>
    <path d="M0,0 H480 V104 C400,104 330,50 230,30 C150,16 60,22 0,36 Z" fill="url(#swooshFill)"/>
    <path d="M0,62 C70,36 190,24 300,44" fill="none" stroke="var(--green)" stroke-width="7" stroke-linecap="round"/>
    <path d="M42,66 C160,34 270,52 350,96 C400,120 445,124 480,122" fill="none" stroke="var(--orange)" stroke-width="6"/>
  </svg>

  <p class="tagline">Making Dreams<br>a Reality</p>

  <p class="phone" aria-label="1300 471 608">
    <span class="d1">1</span><span class="d2">3</span><span class="d3">0</span><span class="d4">0</span><span class="gap"></span><span class="d5">4</span><span class="d2">7</span><span class="d3">1</span><span class="gap"></span><span class="d4">6</span><span class="d6">0</span><span class="d1">8</span>
  </p>

  <p class="contact">
    www.capedcrusadeadventure.com.au<br>
    bookings@capedcrusadeadventure.com.au
  </p>

  <div class="branches">
    <p class="branch branch--fairytale">The Fairytale Gala Adventure</p>
    <p class="branch branch--caped">The Caped Crusade Adventure</p>
  </div>
</section>

</body>
</html>
```